The Jawline Remedy Business Card

Looking for a business card design: front and back. It will be printed at presspanda.example on a leaf cutout trifecta paper with green middle. 3.5 x 2 leaf cutout. It will need bleed room around edges. The front will have my picture, logo, website and email address. The back will be a quote. "Finally. The complete solution to helping you open your mouth fully without pain"
and
"Like Us on Chatterbox to Learn More @ The Jawline Remedy"

Target Market(s)

Women 20-55 years old

Industry/Entity Type

Health Service

Contact Information for Business Card

My photo on one side or embedded, Name: Dr. Marlon Quaid, PT, DPT, MS Website: TheJawlineRemedy.example Email: marlon@keystonemotionclinic.example

Requirements
Must have
• Unique design consistent with my logo

```html
<!DOCTYPE html>
<html lang="en">
<head>
<meta charset="utf-8">
<title>The Jawline Remedy Business Card</title>
<link rel="stylesheet" href="https://fonts.googleapis.com/css2?family=Montserrat:wght@600&family=Roboto:wght@400;500&family=Bebas+Neue&display=swap">
<style>
  :root {
    --backdrop: #e6e7e9;
    --card-dark: #1f2022;
    --photo-dark: #34352f;
    --photo-light: #7d8079;
    --brand-blue: #1f78c8;
    --brand-green: #8cc63f;
    --text-light: #f2f2f2;
    --grad-top: #8cc63f;
    --grad-mid: #3f9a8c;
    --grad-bottom: #1f78c8;
  }
  * { box-sizing: border-box; margin: 0; padding: 0; }
  html, body { width: 1200px; height: 1108px; overflow: hidden; background: var(--backdrop); }
  .stage {
    position: relative; width: 1200px; height: 1108px;
    display: flex; justify-content: center; align-items: center; gap: 80px;
  }
  .card {
    position: relative; width: 400px; height: 700px; border-radius: 22px; overflow: hidden;
    box-shadow: 0 10px 30px rgba(0,0,0,0.18);
  }
  /* Front */
  .card-front { background: var(--card-dark); }
  .brand {
    height: 220px; display: flex; align-items: center; justify-content: center; gap: 18px;
  }
  .brand-mark {
    width: 110px; height: 110px; border-radius: 50%; border: 6px solid var(--brand-blue);
  }
  .brand-name {
    font-family: "Montserrat", sans-serif; font-weight: 600; font-size: 36px; line-height: 1.05;
    color: var(--brand-green);
  }
  .portrait {
    height: 300px;
    background: radial-gradient(ellipse at 55% 40%, var(--photo-light), var(--photo-dark) 70%);
  }
  .contact { padding: 34px 30px 0; font-family: "Roboto", sans-serif; }
  .contact-name { font-size: 28px; font-weight: 500; color: var(--brand-blue); white-space: nowrap; }
  .contact-name .credentials { font-size: 19px; font-weight: 400; color: var(--brand-green); }
  .contact-email { margin-top: 16px; font-size: 16.5px; color: var(--text-light); white-space: nowrap; }
  .contact-web { margin-top: 8px; font-size: 19px; color: var(--brand-green); white-space: nowrap; }
  /* Back */
  .card-back {
    background: linear-gradient(200deg, var(--grad-top) 0%, var(--grad-mid) 55%, var(--grad-bottom) 100%);
    color: #fff; text-align: center;
  }
  .quote {
    margin-top: 150px; padding: 0 20px;
    font-family: "Bebas Neue", sans-serif; font-weight: 400; font-size: 40px; line-height: 1.12;
    text-transform: uppercase; letter-spacing: 0.3px;
  }
  .quote span { display: block; white-space: nowrap; }
  .social {
    position: absolute; left: 0; right: 0; bottom: 80px;
    font-family: "Roboto", sans-serif; font-size: 27px; line-height: 1.25;
  }
  .social-handle { display: flex; align-items: center; justify-content: center; gap: 12px; margin-bottom: 6px; }
  .social-square { width: 46px; height: 46px; background: #fff; border-radius: 4px; flex: none; }
  .social-network { display: flex; flex-direction: column; align-items: flex-start; font-size: 30px; font-weight: 500; line-height: 1.05; }
  .social-label { font-size: 18px; font-weight: 500; }
</style>
</head>
<body>
<main class="stage">
  <section class="card card-front">
    <header class="brand">
      <span class="brand-mark"></span>
      <span class="brand-name">The<br>Jawline<br>Remedy</span>
    </header>
    <div class="portrait" role="img" aria-label="Portrait photo of Dr. Marlon Quaid"></div>
    <div class="contact">
      <p class="contact-name">Dr. Marlon Quaid, <span class="credentials">PT, DPT, MS</span></p>
      <p class="contact-email">marlon@keystonemotionclinic.example</p>
      <p class="contact-web">www.TheJawlineRemedy.example</p>
    </div>
  </section>

  <section class="card card-back">
    <p class="quote">
      <span>Finally. The complete</span>
      <span>solution to helping you</span>
      <span>open your mouth fully</span>
      <span>and eat without jaw pain.</span>
    </p>
    <div class="social">
      <div class="social-handle">
        <span class="social-square"></span>
        <span class="social-network"><span class="social-label">Like us on</span>Chatterbox</span>
      </div>
      <p>to Learn More</p>
      <p>@ The Jawline Remedy</p>
    </div>
  </section>
</main>
</body>
</html>
```